Book Cover for Herb Growing and Ancient Medecine Recipes for People over 50 years

The front book cover shall
- be an eye-catcher even as small as a thumbnail on a cell phone
- contain the following words:
Title: The Patient Gardener's Almanac
Subtitle: Notes from a Quiet Kitchen Shelf
Hook: Effortless fixes for:
• Sleep like never before
• Pain-free movement
• Hair that thrives
• Calm hormones
Author name: Colin Marwether
- meet Pagewell Press print requirements for size, CMYK colors etc.

Attached are covers of best-selling book in my genre.

Target Market(s)

Pagewell book buyers over 50 yrs with some health issues who want to improve their well-being naturally

Colors
00AB8E
00BBA5
67D7C9
C6EFE9
E9F9F6

Requirements
Must have
• a catchy main image

```html
<!DOCTYPE html>
<html lang="en">
<head>
<meta charset="utf-8">
<title>The Patient Gardener's Almanac – Cover</title>
<link rel="stylesheet" href="https://fonts.googleapis.com/css2?family=Anton&family=Archivo:wght@400;700;800&family=Great+Vibes&display=swap">
<style>
  :root {
    --stage: #000000;
    --parchment: #eadcc0;
    --parchment-edge: #d9c39c;
    --frame-dark: #5e5140;
    --frame-mid: #8f806a;
    --frame-light: #cfc4ae;
    --frame-pale: #e4dccb;
    --ink-white: #ffffff;
    --ink-soft: #ece8e2;
    --author: #e4d0b0;
    --rule: rgba(255,255,255,0.75);
  }
  * { margin: 0; padding: 0; box-sizing: border-box; }
  html, body { width: 922px; height: 1200px; overflow: hidden; background: var(--stage); }
  .canvas { position: relative; width: 922px; height: 1200px; background: var(--stage); }

  .parchment {
    position: absolute; left: 122px; top: 154px; width: 667px; height: 928px;
    background: radial-gradient(ellipse at 50% 45%, var(--parchment) 55%, var(--parchment-edge) 100%);
  }

  .frame {
    position: absolute; left: 165px; top: 188px; width: 584px; height: 844px;
    background: linear-gradient(135deg, var(--frame-mid), var(--frame-dark) 40%, var(--frame-mid) 70%, var(--frame-dark));
    box-shadow: 0 4px 10px rgba(60,40,20,0.45);
  }
  .frame-band {
    position: absolute; inset: 18px;
    background: linear-gradient(135deg, var(--frame-pale), var(--frame-light) 45%, var(--frame-mid));
    border: 2px solid var(--frame-dark);
  }
  .frame-lip {
    position: absolute; inset: 52px 50px 54px 50px;
    background: var(--frame-dark);
    border: 3px solid var(--frame-light);
  }

  .spice-photo {
    position: absolute; left: 238px; top: 262px; width: 439px; height: 694px;
    background:
      radial-gradient(circle at 30% 10%, rgba(160,40,30,0.55), transparent 18%),
      radial-gradient(circle at 80% 10%, rgba(190,140,20,0.55), transparent 18%),
      radial-gradient(circle at 55% 55%, rgba(90,100,50,0.45), transparent 25%),
      radial-gradient(circle at 40% 72%, rgba(130,30,50,0.45), transparent 18%),
      radial-gradient(circle at 75% 82%, rgba(110,95,40,0.5), transparent 20%),
      radial-gradient(circle at 20% 60%, rgba(90,60,40,0.5), transparent 22%),
      linear-gradient(180deg, #2e261c, #1c1712 60%, #15110d);
  }

  .cover-text {
    position: absolute; left: 238px; top: 262px; width: 439px; height: 694px;
    color: var(--ink-white); text-align: center;
  }
  .title-the {
    position: absolute; left: 0; right: 0; top: 82px;
    font-family: "Great Vibes", cursive; font-size: 48px; line-height: 1;
    padding-left: 10px;
  }
  .title-upper {
    position: absolute; left: 0; right: 0; top: 130px;
    font-family: "Anton", sans-serif; font-size: 38px; line-height: 1; letter-spacing: 0.5px;
  }
  .title-main {
    position: absolute; left: 0; right: 0; top: 170px;
    font-family: "Anton", sans-serif; font-size: 92px; line-height: 1.05;
  }
  .subtitle {
    position: absolute; left: 0; right: 0; top: 263px;
    font-family: "Archivo", sans-serif; font-weight: 800; font-size: 15px;
    letter-spacing: 0.2px; color: var(--ink-soft);
  }
  .hook {
    position: absolute; left: 55px; right: 55px; top: 293px;
    display: flex; align-items: center; gap: 10px;
    font-family: "Archivo", sans-serif; font-size: 11px; color: var(--ink-soft);
  }
  .hook::before, .hook::after { content: ""; flex: 1; height: 1px; background: var(--rule); }
  .benefits {
    position: absolute; left: 44px; right: 40px; top: 324px;
    display: flex; list-style: none;
    font-family: "Archivo", sans-serif; font-size: 11px; line-height: 14px; color: var(--ink-soft);
  }
  .benefits li { flex: 1; padding: 6px 2px; }
  .benefits li + li { border-left: 1px solid var(--rule); }
  .author {
    position: absolute; left: 0; right: 0; top: 619px;
    font-family: "Archivo", sans-serif; font-weight: 800; font-size: 28px;
    letter-spacing: 1.5px; color: var(--author);
  }
</style>
</head>
<body>
<div class="canvas">
  <div class="parchment"></div>
  <div class="frame">
    <div class="frame-band"></div>
    <div class="frame-lip"></div>
  </div>
  <div class="spice-photo" role="img" aria-label="Overhead photograph of many bowls of dried herbs and spices in red, green, ochre and brown tones"></div>
  <div class="cover-text">
    <div class="title-the">The</div>
    <h1 class="title-upper">PATIENT GARDENER'S</h1>
    <div class="title-main">ALMANAC</div>
    <p class="subtitle">NOTES FROM A QUIET KITCHEN SHELF</p>
    <p class="hook">EFFORTLESS FIXES FOR</p>
    <ul class="benefits">
      <li>SLEEP LIKE<br>NEVER BEFORE</li>
      <li>PAIN-FREE<br>MOVEMENT</li>
      <li>HAIR THAT<br>THRIVES</li>
      <li>CALM<br>HORMONES</li>
    </ul>
    <p class="author">COLIN MARWETHER</p>
  </div>
</div>
</body>
</html>
```